Flyer with pull tabs

This project is to redo/update my pull tab flier
The Top line should be Need Health Insurance?
Please add as many images as in the design as possible.
The size should be 8.5 X 11 size
The information needs to be with BrightPath Insurance Services LLC information.
You will use the phone number (713) 555-0187 and the email address Doreen@CoverageGalPlans.example
The slogan is “Simplifying the Benefits Solution Process”
Life | Health | Retirement | Long-Term Care

```html
<!DOCTYPE html>
<html lang="en">
<head>
<meta charset="utf-8">
<title>Need Health Insurance? – BrightPath Insurance Services</title>
<link rel="stylesheet" href="https://fonts.googleapis.com/css2?family=Didact+Gothic&family=Montserrat:wght@600;700;800&display=swap">
<style>
  :root {
    --band-light: #a59dca;
    --band-dark: #7462a0;
    --teal-light: #33cccc;
    --teal: #009999;
    --indigo: #666699;
    --lavender: #a7a0c6;
    --ink: #111;
    --accent-text: #5e5a9a;
    --tile-blank: #f4f2ec;
    --paper: #fff;
  }
  * { box-sizing: border-box; margin: 0; padding: 0; }
  html, body { width: 927px; height: 1200px; overflow: hidden; background: var(--paper); }
  .flyer {
    position: relative; width: 927px; height: 1200px;
    font-family: "Didact Gothic", "Century Gothic", sans-serif; color: var(--ink);
  }
  .headline-band {
    position: absolute; left: 0; top: 0; width: 927px; height: 259px;
    background: linear-gradient(90deg, var(--band-light), var(--band-dark));
    box-shadow: 0 8px 12px rgba(0,0,0,.25);
    display: flex; flex-direction: column; align-items: center; justify-content: center;
  }
  .headline {
    font-family: "Montserrat", sans-serif; font-weight: 600; color: #fff;
    font-size: 108px; line-height: 110px; text-align: center; letter-spacing: 1px;
    padding-top: 6px;
  }
  .tagline {
    position: absolute; left: 0; width: 927px; top: 280px; text-align: center;
    font-size: 36px; letter-spacing: 1px; color: var(--accent-text);
  }
  .tagline strong { font-family: "Montserrat", sans-serif; font-weight: 700; }
  .photo-strip {
    position: absolute; left: 92px; top: 336px; width: 760px; height: 186px;
    display: grid; grid-template-columns: repeat(8, 1fr); grid-template-rows: 1fr 1fr; gap: 1px;
  }
  .tile { background: var(--tile-blank); }
  .tile--teal { background: var(--teal-light); }
  .tile--lavender { background: var(--lavender); }
  .tile--photo { background: linear-gradient(135deg, #c9b4a0, #8a7a6e); }
  .tile--wide { grid-column: span 2; background: linear-gradient(135deg, #9fb3c9, #6d6a66); }
  .tile--tall { grid-row: span 2; background: linear-gradient(160deg, #d8b79c, #4f6f9a); }
  .intro {
    position: absolute; left: 0; width: 927px; top: 541px; text-align: center; font-size: 28px;
  }
  .services {
    position: absolute; left: 0; width: 927px; top: 584px; text-align: center; font-size: 27px;
  }
  .services .dot {
    display: inline-block; width: 8px; height: 8px; background: var(--teal);
    margin: 0 20px; vertical-align: middle;
  }
  .invite {
    position: absolute; left: 0; width: 927px; top: 650px; text-align: center;
    font-size: 20px; color: var(--accent-text);
  }
  .agent-photo {
    position: absolute; left: 91px; top: 707px; width: 111px; height: 132px;
    background: linear-gradient(180deg, #e9e4de, #3a2a24);
  }
  .agent-details { position: absolute; left: 210px; top: 704px; }
  .agent-name { font-family: "Montserrat", sans-serif; font-weight: 800; font-size: 25px; line-height: 30px; }
  .agent-title { font-size: 17px; line-height: 20px; }
  .agent-phone { font-family: "Montserrat", sans-serif; font-weight: 800; font-size: 26px; line-height: 34px; }
  .agent-email { font-size: 17px; line-height: 20px; }
  .slogan {
    position: absolute; left: 520px; width: 352px; top: 700px; text-align: center;
    font-family: "Montserrat", sans-serif; font-weight: 700; font-size: 21px; line-height: 28px;
  }
  .brand { position: absolute; left: 600px; top: 808px; display: flex; align-items: center; gap: 10px; }
  .brand-mark { width: 26px; height: 26px; border-radius: 50%; background: var(--teal-light); }
  .brand-name { font-size: 30px; color: var(--indigo); }
  .license { position: absolute; left: 91px; top: 893px; font-size: 13px; }
  .lines-of-business {
    position: absolute; right: 78px; top: 893px; font-size: 13px; color: var(--accent-text); letter-spacing: .3px;
  }
  .color-bars { position: absolute; top: 922px; height: 22px; left: 0; width: 927px; }
  .color-bars span { position: absolute; top: 0; height: 22px; }
  .pull-tabs { position: absolute; left: 91px; top: 961px; width: 758px; height: 226px; display: flex; }
  .tab {
    flex: 1; border-left: 1.5px dashed var(--ink); display: flex; justify-content: center;
    writing-mode: vertical-rl; font-size: 12.5px; line-height: 17px; padding-top: 2px;
  }
  .tab:last-child { border-right: 1.5px dashed var(--ink); }
</style>
</head>
<body>
<div class="flyer">
  <header class="headline-band">
    <h1 class="headline">NEED HEALTH<br>INSURANCE?</h1>
  </header>

  <p class="tagline">AFFORDABLE SOLUTIONS CENTERED AROUND <strong>YOU</strong>.</p>

  <div class="photo-strip">
    <div class="tile tile--teal"></div>
    <div class="tile tile--wide" role="img" aria-label="Smiling contractor in front of a house under construction"></div>
    <div class="tile"></div>
    <div class="tile tile--photo" role="img" aria-label="Smiling couple"></div>
    <div class="tile"></div>
    <div class="tile tile--tall" role="img" aria-label="Young family with a sleeping baby"></div>
    <div class="tile"></div>
    <div class="tile"></div>
    <div class="tile tile--photo" role="img" aria-label="Mother and son smiling"></div>
    <div class="tile"></div>
    <div class="tile tile--photo" role="img" aria-label="Smiling chef in a white hat"></div>
    <div class="tile"></div>
    <div class="tile tile--photo" role="img" aria-label="Businessman in shirt and tie"></div>
    <div class="tile tile--lavender"></div>
  </div>

  <p class="intro">Helping our local small businesses, families, and individuals.</p>
  <p class="services">Health<span class="dot"></span>Dental<span class="dot"></span>Vision<span class="dot"></span>Disability<span class="dot"></span>And More!</p>
  <p class="invite">For personalized service in your area, contact your local BrightPath agent today.</p>

  <div class="agent-photo" role="img" aria-label="Portrait of the insurance agent"></div>
  <div class="agent-details">
    <p class="agent-name">DOREEN WHITFIELD</p>
    <p class="agent-title">Licensed Insurance Agent</p>
    <p class="agent-phone">713-555-0187</p>
    <p class="agent-email">Doreen@CoverageGalPlans.example</p>
  </div>

  <p class="slogan">SIMPLIFYING THE<br>BENEFITS SOLUTION PROCESS</p>
  <div class="brand">
    <span class="brand-mark"></span>
    <span class="brand-name">BrightPath</span>
  </div>

  <p class="license">BrightPath Insurance Services LLC 1048362</p>
  <p class="lines-of-business">LIFE&nbsp; |&nbsp; HEALTH&nbsp; |&nbsp; RETIREMENT&nbsp; |&nbsp; LONG-TERM CARE</p>

  <div class="color-bars">
    <span style="left:91px;width:193px;background:var(--teal-light)"></span>
    <span style="left:289px;width:180px;background:var(--teal)"></span>
    <span style="left:474px;width:183px;background:var(--indigo)"></span>
    <span style="left:663px;width:186px;background:var(--lavender)"></span>
  </div>

  <div class="pull-tabs">
    <div class="tab"><span>Insurance Solutions<br>(713) 555-0187<br>Doreen@CoverageGalPlans.example</span></div>
    <div class="tab"><span>Insurance Solutions<br>(713) 555-0187<br>Doreen@CoverageGalPlans.example</span></div>
    <div class="tab"><span>Insurance Solutions<br>(713) 555-0187<br>Doreen@CoverageGalPlans.example</span></div>
    <div class="tab"><span>Insurance Solutions<br>(713) 555-0187<br>Doreen@CoverageGalPlans.example</span></div>
    <div class="tab"><span>Insurance Solutions<br>(713) 555-0187<br>Doreen@CoverageGalPlans.example</span></div>
    <div class="tab"><span>Insurance Solutions<br>(713) 555-0187<br>Doreen@CoverageGalPlans.example</span></div>
    <div class="tab"><span>Insurance Solutions<br>(713) 555-0187<br>Doreen@CoverageGalPlans.example</span></div>
    <div class="tab"><span>Insurance Solutions<br>(713) 555-0187<br>Doreen@CoverageGalPlans.example</span></div>
    <div class="tab"><span>Insurance Solutions<br>(713) 555-0187<br>Doreen@CoverageGalPlans.example</span></div>
  </div>
</div>
</body>
</html>
```